Summer Sale Graphics for Social Media

I want to create 11 social media graphics (new Instagram size 4:5 (1080 x 1350 pixels) focusing on our Summer Sale Graphics, using any of the pics attached. Use the attached pics, NO RANDOM STOCK PHOTOGRAPHY. For the color scheme of the graphics, they should all be complementary to the product colors in the photos.
You can add any of the photos attached but none are required. You can do some of the graphics in all text. I mainly need BOLD text that says one of the headlines (11 total) SEE ATTACHED WORD DOCUMENT for the headlines to use.

```html
<!DOCTYPE html>
<html lang="en">
<head>
<meta charset="utf-8">
<title>Summer Sale Social Graphics</title>
<link rel="stylesheet" href="https://fonts.googleapis.com/css2?family=Barlow:wght@800&family=Barlow+Condensed:wght@700&family=Barlow+Semi+Condensed:wght@700;800&display=swap">
<style>
  :root {
    --page: #ffffff;
    --mint: #9dd5b6;
    --coral: #ff7452;
    --sun: #fff03d;
    --ocean: #146aaa;
    --white: #ffffff;
  }
  * { margin: 0; padding: 0; box-sizing: border-box; }
  html, body {
    width: 1200px;
    height: 753px;
    overflow: hidden;
    background: var(--page);
  }
  .board {
    position: relative;
    width: 1200px;
    height: 753px;
  }
  .post {
    position: absolute;
    top: 70px;
    width: 488px;
    height: 610px;
    overflow: hidden;
  }
  .post--mint { left: 75px; background: var(--mint); }
  .post--coral { left: 633px; background: var(--coral); }

  .photo {
    position: absolute;
    z-index: 1;
  }
  .post--mint .photo {
    left: 80px;
    top: 28px;
    width: 408px;
    height: 582px;
    background: linear-gradient(180deg, rgba(245,245,245,0.0) 0%, rgba(235,235,235,0.55) 40%, rgba(40,40,40,0.35) 78%, rgba(240,240,240,0.9) 100%);
    border-radius: 120px 120px 0 0;
  }
  .post--coral .photo {
    left: 215px;
    top: 45px;
    width: 268px;
    height: 565px;
    background: linear-gradient(180deg, rgba(120,80,60,0.25) 0%, rgba(150,100,75,0.6) 45%, rgba(25,25,25,0.7) 100%);
    border-radius: 110px 110px 0 0;
  }

  .copy {
    position: absolute;
    z-index: 2;
    left: 22px;
  }
  .post--mint .copy { top: 75px; }
  .post--coral .copy { top: 46px; }

  .offer {
    font-family: "Barlow", sans-serif;
    font-weight: 800;
    color: var(--sun);
    line-height: 1;
    letter-spacing: 0.2px;
  }
  .post--mint .offer { font-size: 25px; }
  .post--coral .offer { font-size: 28px; }

  .headline {
    color: var(--white);
    text-transform: uppercase;
  }
  .post--mint .headline {
    font-family: "Barlow Condensed", sans-serif;
    font-weight: 700;
    font-size: 62px;
    line-height: 52px;
    margin-top: 14px;
  }
  .post--coral .headline {
    font-family: "Barlow Semi Condensed", sans-serif;
    font-weight: 800;
    font-size: 82px;
    line-height: 65.5px;
    margin-top: 12px;
  }

  .cta {
    text-transform: uppercase;
  }
  .post--mint .cta {
    font-family: "Barlow Semi Condensed", sans-serif;
    font-weight: 800;
    color: var(--ocean);
    font-size: 94px;
    line-height: 80px;
    margin-top: 14px;
  }
  .post--coral .cta {
    font-family: "Barlow Semi Condensed", sans-serif;
    font-weight: 800;
    color: var(--sun);
    font-size: 90px;
    line-height: 75px;
    margin-top: 14px;
  }
</style>
</head>
<body>
  <main class="board">
    <section class="post post--mint">
      <div class="photo" role="img" aria-label="Smiling woman in a white cropped sweater pointing down at a row of supplement bottles and cream pumps on a marble counter"></div>
      <div class="copy">
        <p class="offer">UP TO $15 OFF</p>
        <h2 class="headline">Final<br>Countdown<br>to Summer</h2>
        <p class="cta">Sale<br>Now!</p>
      </div>
    </section>

    <section class="post post--coral">
      <div class="photo" role="img" aria-label="Smiling woman in a sparkling brown mesh top and black jeans holding three supplement bottles"></div>
      <div class="copy">
        <p class="offer">UP TO $15 OFF</p>
        <h2 class="headline">Your<br>Summer<br>Body<br>Won’t<br>Wait</h2>
        <p class="cta">Sale<br>Now!</p>
      </div>
    </section>
  </main>
</body>
</html>
```